I need a simple, classy and stylish business card. I would like it to have a black background with white writing. I would like you to use my logo you designed on the front with the word 'Imagery" used underneath it in the same font. On the back I was thinking of the website at the top 'tormavine.com' Then my social media accounts, Can you use the instagram, Facebook and twitter logo then my handles?
Please let me know what you think.
Regards Lars
Industry/Entity Type
Business
Requirements
Must have
- Website: www.tormavine.com
- Social media handles..
- Instagram: @Lars_Tormavine_Imagery
- Facebook: Lars Tormavine Imagery
- Twitter: @Lars_Tormavin
- Email: info@tormavin.com
- Phone: 0473 518 609

```html
<!DOCTYPE html>
<html lang="en">
<head>
<meta charset="utf-8">
<title>Lars Tormavine Imagery – Business Card</title>
<link rel="stylesheet" href="https://fonts.googleapis.com/css2?family=Open+Sans:wght@300;400;700&display=swap">
<style>
  :root {
    --backdrop: #383838;
    --card: #000000;
    --ink: #ffffff;
    --rule: #8a8a8a;
    --shadow: rgba(0, 0, 0, 0.55);
  }
  * { margin: 0; padding: 0; box-sizing: border-box; }
  html, body {
    width: 1054px;
    height: 1200px;
    overflow: hidden;
    background: var(--backdrop);
    font-family: "Open Sans", sans-serif;
    color: var(--ink);
  }
  .card {
    position: absolute;
    background: var(--card);
    border-radius: 12px;
    box-shadow: 0 6px 14px var(--shadow);
  }
  .card--front { left: 141px; top: 153px; width: 772px; height: 427px; }
  .card--back  { left: 146px; top: 621px; width: 766px; height: 423px; }

  .brand-mark {
    position: absolute;
    border-radius: 50%;
    border: 3px solid var(--ink);
  }
  .brand-name {
    position: absolute;
    font-weight: 300;
    white-space: nowrap;
    line-height: 1;
  }
  .card--front .brand-mark { left: 165px; top: 155px; width: 118px; height: 118px; }
  .card--front .brand-name { left: 302px; top: 188px; font-size: 50px; }

  .tagline {
    position: absolute;
    left: 0; right: 0; top: 327px;
    display: flex;
    align-items: center;
    justify-content: center;
    gap: 18px;
    font-weight: 300;
    font-size: 30px;
    line-height: 1;
  }
  .tagline__rule {
    width: 66px;
    height: 1px;
    background: linear-gradient(90deg, transparent, var(--rule));
  }
  .tagline__rule--end { background: linear-gradient(90deg, var(--rule), transparent); }

  .card--back .brand-mark { left: 31px; top: 38px; width: 64px; height: 64px; border-width: 2px; }
  .card--back .brand-name { left: 111px; top: 53px; font-size: 28px; }

  .holder-name {
    position: absolute;
    right: 45px; top: 100px;
    font-size: 26px;
    font-weight: 400;
    line-height: 1;
  }
  .holder-name strong { font-weight: 700; }

  .contact-list {
    position: absolute;
    left: 42px; top: 262px;
    list-style: none;
  }
  .contact-list li {
    display: flex;
    align-items: center;
    gap: 12px;
    height: 34px;
    font-size: 21px;
  }
  .contact-list svg { width: 22px; height: 22px; flex: none; }

  .social-list {
    position: absolute;
    left: 30px; top: 383px;
    display: flex;
    gap: 24px;
    list-style: none;
    font-size: 18px;
  }
  .social-list li { display: flex; align-items: center; gap: 8px; }
  .social-dot {
    width: 22px; height: 22px;
    border-radius: 50%;
    background: var(--ink);
    flex: none;
  }
</style>
</head>
<body>

<section class="card card--front" aria-label="Card front">
  <span class="brand-mark" aria-hidden="true"></span>
  <span class="brand-name">Lars Tormavine</span>
  <div class="tagline">
    <span class="tagline__rule"></span>
    <span class="tagline__word">Imagery</span>
    <span class="tagline__rule tagline__rule--end"></span>
  </div>
</section>

<section class="card card--back" aria-label="Card back">
  <span class="brand-mark" aria-hidden="true"></span>
  <span class="brand-name">Lars Tormavine</span>
  <p class="holder-name"><strong>Your</strong> Name</p>

  <ul class="contact-list">
    <li>
      <svg viewBox="0 0 22 22" fill="none" stroke="currentColor" stroke-width="1.4" aria-hidden="true">
        <circle cx="11" cy="11" r="9.5"/>
        <path d="M8 6.5l1.6 2.2-1 1.1c.6 1.4 1.6 2.4 3 3l1.1-1 2.2 1.6-.8 1.4c-3.6-.4-6.3-3.1-6.7-6.7z" fill="currentColor" stroke="none"/>
      </svg>
      <span>0473 518 609</span>
    </li>
    <li>
      <svg viewBox="0 0 22 22" fill="none" stroke="currentColor" stroke-width="1.4" aria-hidden="true">
        <rect x="2" y="5" width="18" height="12"/>
        <path d="M2 5l9 7 9-7M2 17l6.5-6M20 17l-6.5-6"/>
      </svg>
      <span>info@tormavine.com</span>
    </li>
    <li>
      <svg viewBox="0 0 22 22" fill="none" stroke="currentColor" stroke-width="1.3" aria-hidden="true">
        <circle cx="11" cy="11" r="9"/>
        <ellipse cx="11" cy="11" rx="4" ry="9"/>
        <path d="M2 11h18M3.5 6.5h15M3.5 15.5h15"/>
      </svg>
      <span>www.tormavine.com</span>
    </li>
  </ul>

  <ul class="social-list">
    <li><span class="social-dot" aria-hidden="true"></span><span>@LarsTormavineImagery</span></li>
    <li><span class="social-dot" aria-hidden="true"></span><span>@Lars_Tormavin</span></li>
    <li><span class="social-dot" aria-hidden="true"></span><span>@Lars_Tormavine_Imagery</span></li>
  </ul>
</section>

</body>
</html>
```